Surface Protection company needs cards

We are a New Zealand company that will apply nanotechnology coatings on surfaces to prevent growth and spread of bacteria, viruses, mold etc with a sprayer. We deal with large corporates, airlines, hospitals and schools so we are after a new modern, simple and clean look that will have great visual impact.
We a company that is focused on prevention and protection.

Company name, Vela Shield

Subtext, Antimicrobial Surface Protection

Logo, VS

Target Market(s)

Hospitals, Transport agencies, Airlines, Corporate entities

Contact Information for Business Card

Company name, VelaShield
Logo, VS

Gareth Tolley
velashieldnz@postbox.example
+64219305562
www.velashield.example.nz

Requirements
Must have
• Simple clean look.
Nice to have
• We apply nano coatings so try and incorporate this into a theme somehow

```html
<!DOCTYPE html>
<html lang="en">
<head>
<meta charset="utf-8">
<title>VelaShield Business Cards</title>
<link href="https://fonts.googleapis.com/css2?family=Montserrat:wght@300;400;600;700&display=swap" rel="stylesheet">
<style>
  :root {
    --canvas-bg: #e6e6e8;
    --card-dark: #000000;
    --card-light: #ffffff;
    --ink: #1e1e1e;
    --ink-soft: #555555;
    --mark-grey: #d4d4d4;
    --accent-grey: #b9b9b9;
  }
  * { margin: 0; padding: 0; box-sizing: border-box; }
  html, body {
    width: 1200px;
    height: 1200px;
    overflow: hidden;
  }
  body {
    background: var(--canvas-bg);
    font-family: "Montserrat", sans-serif;
    position: relative;
  }
  .card {
    position: absolute;
    left: 251px;
    width: 700px;
    height: 398px;
  }
  .card--front {
    top: 148px;
    background: var(--card-dark);
    color: var(--card-light);
  }
  .card--back {
    top: 652px;
    background: var(--card-light);
    color: var(--ink);
  }
  .front-monogram {
    position: absolute;
    top: 150px;
    left: 0;
    width: 100%;
    text-align: center;
    font-weight: 600;
    font-size: 104px;
    line-height: 1;
    letter-spacing: -2px;
    color: var(--mark-grey);
  }
  .front-url {
    position: absolute;
    top: 288px;
    left: 0;
    width: 100%;
    text-align: center;
    font-weight: 400;
    font-size: 20px;
    letter-spacing: 0.3px;
  }
  .contact {
    position: absolute;
    right: 70px;
    top: 48px;
    text-align: right;
  }
  .contact__name {
    font-weight: 700;
    font-size: 22px;
    margin-bottom: 12px;
  }
  .contact__line {
    font-weight: 400;
    font-size: 21px;
    line-height: 29px;
    letter-spacing: 0.3px;
  }
  .brand {
    position: absolute;
    left: 74px;
    top: 214px;
  }
  .brand__row {
    display: flex;
    align-items: center;
    gap: 12px;
  }
  .brand__dot {
    width: 30px;
    height: 30px;
    border-radius: 50%;
    background: var(--accent-grey);
  }
  .brand__name {
    font-weight: 600;
    font-size: 40px;
    line-height: 1;
    color: var(--ink);
  }
  .brand__tagline {
    margin-top: 6px;
    font-weight: 300;
    font-size: 19.5px;
    color: var(--ink-soft);
    letter-spacing: 0.4px;
  }
  .back-url {
    position: absolute;
    left: 80px;
    top: 310px;
    font-weight: 400;
    font-size: 20px;
    letter-spacing: 0.3px;
  }
</style>
</head>
<body>
  <section class="card card--front">
    <div class="front-monogram">VS</div>
    <div class="front-url">www.velashield.example.nz</div>
  </section>

  <section class="card card--back">
    <div class="contact">
      <div class="contact__name">Gareth Tolley</div>
      <div class="contact__line">velashieldnz@postbox.example</div>
      <div class="contact__line">+64219305562</div>
    </div>
    <div class="brand">
      <div class="brand__row">
        <span class="brand__dot"></span>
        <span class="brand__name">VelaShield</span>
      </div>
      <div class="brand__tagline">Antimicrobial Surface Protection</div>
    </div>
    <div class="back-url">www.velashield.example.nz</div>
  </section>
</body>
</html>
```